Keepers of the Salt Roads book cover

My goal is to choose a submission ready cover for my self-published book. I am looking for an illustrative design that coordinates with the mood of the book, and with current market expectations.

Attached for context are three prior drafts of the cover. My desire is for something more illustrative (like the first one) than obvious AI, like the other two. The story takes place in a fictional town in the Arizona desert. The landscape is a big part of the story. So I would like the mood and color palette to reflect the desert. Reflect; not be a photorealistic depiction of desert. It need not portray the desert explicitly at all, if the design can invoke it. The book does have a fantasy story, but I do not want a "fantasy book" cover. Something more contemporary in design and font choices.

For example, this cover invokes the sea: https://www.bookvarnel.example/item/47213

This one invokes a forest at night: https://www.bookvarnel.example/item/58324

And this one a different take on the sea: https://www.bookvarnel.example/item/69435

(By the way, my book with its current cover, which I hate, is at:)
https://www.bookvarnel.example/item/70546

Target Market(s)

25-80 year old, professional females.

Font styles to use
Other font styles liked:
• For the Author Name, use upper and lower case (i.e., Dale Worthen), with Abadi font, if possible. In the title, make "of the" lower case.

Requirements
Must have
• Copper Wren logo on the spine, with the words "Copper Wren" beneath it.

```html
<!DOCTYPE html>
<html lang="en">
<head>
<meta charset="utf-8">
<title>Keepers of the Salt Roads — Cover</title>
<link rel="stylesheet" href="https://fonts.googleapis.com/css2?family=Source+Serif+4:opsz,wght@8..60,700&display=swap">
<style>
  :root {
    --stage: #1a1812;
    --title-dark: #7a2a17;
    --title-red: #b8170e;
    --author-cream: #f2e0c0;
    --sky-teal: #7dbfae;
    --sky-mist: #b9d8c0;
    --sky-cream: #ece4c4;
    --sun-cream: #f4e6bb;
    --dune-orange: #d8642a;
    --dune-red: #c02a10;
    --dune-crimson: #a3190c;
    --dune-deep: #5a0a06;
  }
  * { margin: 0; padding: 0; box-sizing: border-box; }
  html, body {
    width: 1200px;
    height: 846px;
    overflow: hidden;
    background: var(--stage);
  }
  .book-cover {
    position: absolute;
    left: 356px;
    top: 33px;
    width: 488px;
    height: 781px;
    overflow: hidden;
    box-shadow: 0 10px 30px rgba(0, 0, 0, 0.6);
  }
  .cover-art {
    position: absolute;
    inset: 0;
    width: 100%;
    height: 100%;
  }
  .cover-text {
    position: absolute;
    left: 0;
    width: 100%;
    text-align: center;
    font-family: "Source Serif 4", Georgia, serif;
    font-weight: 700;
    line-height: 1;
    white-space: nowrap;
  }
  .title-lead   { top: 84px;  font-size: 60px; color: var(--title-dark); letter-spacing: 0.5px; }
  .title-joiner { top: 157px; font-size: 33px; color: var(--title-dark); }
  .title-main   { font-size: 114px; color: var(--title-red); }
  .title-main.line-one { top: 194px; }
  .title-main.line-two { top: 293px; }
  .author-name  { top: 690px; font-size: 42px; color: var(--author-cream); }
</style>
</head>
<body>
  <main class="book-cover">
    <svg class="cover-art" viewBox="0 0 488 781" role="img"
         aria-label="Illustrated desert at sunset: teal sky fading to cream, a pale setting sun behind rock buttes, and layered red dunes dotted with saguaro cacti">
      <defs>
        <linearGradient id="skyTones" x1="0" y1="0" x2="0" y2="1">
          <stop offset="0" stop-color="var(--sky-teal)"/>
          <stop offset="0.35" stop-color="var(--sky-mist)"/>
          <stop offset="0.7" stop-color="var(--sky-cream)"/>
          <stop offset="1" stop-color="#efdcae"/>
        </linearGradient>
        <radialGradient id="sunGlow" cx="244" cy="520" r="150" gradientUnits="userSpaceOnUse">
          <stop offset="0" stop-color="var(--sun-cream)" stop-opacity="0.9"/>
          <stop offset="0.7" stop-color="var(--sun-cream)" stop-opacity="0.5"/>
          <stop offset="1" stop-color="var(--sun-cream)" stop-opacity="0"/>
        </radialGradient>
        <linearGradient id="duneTones" x1="0" y1="0" x2="0" y2="1">
          <stop offset="0" stop-color="var(--dune-orange)"/>
          <stop offset="0.25" stop-color="var(--dune-red)"/>
          <stop offset="0.65" stop-color="var(--dune-crimson)"/>
          <stop offset="1" stop-color="var(--dune-deep)"/>
        </linearGradient>
      </defs>
      <rect class="sky" width="488" height="560" fill="url(#skyTones)"/>
      <rect class="sun" width="488" height="560" fill="url(#sunGlow)"/>
      <path class="dunes" d="M0 540 C120 520 260 545 360 525 C420 514 460 516 488 520 L488 781 L0 781 Z" fill="url(#duneTones)"/>
    </svg>

    <h1>
      <span class="cover-text title-lead">KEEPERS</span>
      <span class="cover-text title-joiner">of the</span>
      <span class="cover-text title-main line-one">SALT</span>
      <span class="cover-text title-main line-two">ROADS</span>
    </h1>
    <p class="cover-text author-name">Dale Worthen</p>
  </main>
</body>
</html>
```